Electronic hardware design and manufacturer needing a new business card design.

We need a new business card design consisting of a double sided design adhering to brand and logo guidelines attached. I also want to incorporate something that recognizes our 25th year in business ("EST 2001" or something like that....).

```html
<!DOCTYPE html>
<html lang="en">
<head>
<meta charset="utf-8">
<title>Northridge Telemetry Co. – Business Card</title>
<link rel="stylesheet" href="https://fonts.googleapis.com/css2?family=Montserrat:wght@400;500;600;700;800&display=swap">
<style>
  :root {
    --stage: #1b1b1e;
    --card: #232326;
    --card-edge: #2c2c30;
    --brand-grey: #8a8a8f;
    --brand-blue: #8fa9d6;
    --text-light: #d9dbe0;
    --navy: #12324a;
    --green: #7cc242;
    --orange: #f26b21;
    --amber: #f7a81b;
    --white: #ffffff;
  }
  * { box-sizing: border-box; margin: 0; padding: 0; }
  html, body {
    width: 1200px; height: 800px; overflow: hidden;
    background: var(--stage);
    font-family: "Montserrat", sans-serif;
  }
  .sheet {
    width: 1200px; height: 800px;
    display: flex; flex-direction: column;
    align-items: center; justify-content: center; gap: 28px;
  }
  .card {
    position: relative;
    width: 640px; height: 366px;
    background: var(--card);
    border: 1px solid var(--card-edge);
    border-radius: 4px;
    box-shadow: 0 10px 30px rgba(0,0,0,.45);
  }

  /* Front */
  .card--front { display: flex; align-items: center; justify-content: center; }
  .brand { display: flex; align-items: center; gap: 12px; }
  .brand__mark { width: 18px; height: 18px; }
  .brand__name { font-weight: 700; letter-spacing: .02em; }
  .card--front .brand__mark { background: var(--brand-grey); }
  .card--front .brand__name { color: var(--brand-grey); font-size: 30px; }

  /* Back */
  .card--back .brand { position: absolute; top: 40px; right: 40px; }
  .card--back .brand__mark { background: var(--brand-blue); width: 14px; height: 14px; }
  .card--back .brand__name { color: var(--brand-blue); font-size: 20px; }

  .contact { position: absolute; left: 44px; top: 100px; }
  .contact__name { color: var(--brand-blue); font-weight: 600; font-size: 26px; line-height: 1.1; }
  .contact__role { color: var(--text-light); font-size: 16px; font-weight: 500; margin-top: 2px; }
  .contact__list { list-style: none; margin-top: 14px; }
  .contact__item {
    display: flex; align-items: center; gap: 9px;
    color: var(--text-light); font-size: 13px; line-height: 22px;
  }
  .contact__icon { width: 15px; height: 15px; flex: none; }

  .products {
    position: absolute; left: 44px; right: 40px; bottom: 34px;
    display: grid; grid-template-columns: repeat(3, 1fr); row-gap: 18px; column-gap: 16px;
  }
  .product { display: flex; align-items: center; gap: 8px; }
  .product__mark { width: 26px; height: 26px; border-radius: 5px; flex: none; }
  .product__name { font-weight: 800; font-size: 22px; line-height: 1; }
  .product__tag { font-size: 7.5px; font-weight: 600; letter-spacing: .04em; color: var(--text-light); margin-top: 3px; text-transform: uppercase; }

  .product--scope .product__mark { background: var(--navy); }
  .product--scope .product__name { color: var(--white); }
  .product--beacon .product__mark { background: var(--orange); }
  .product--beacon .product__name { color: var(--orange); }
  .product--tether .product__mark { background: var(--navy); }
  .product--tether .product__name { color: var(--white); }
  .product--drover .product__mark { background: var(--green); }
  .product--drover .product__name { color: var(--green); }
  .product--strider .product__mark { background: var(--amber); }
  .product--strider .product__name { color: var(--amber); }
</style>
</head>
<body>
<main class="sheet">

  <section class="card card--front" aria-label="Card front">
    <div class="brand">
      <span class="brand__mark"></span>
      <span class="brand__name">Northridge Telemetry Co.</span>
    </div>
  </section>

  <section class="card card--back" aria-label="Card back">
    <div class="brand">
      <span class="brand__mark"></span>
      <span class="brand__name">Northridge Telemetry Co.</span>
    </div>

    <div class="contact">
      <p class="contact__name">Marcus Hale</p>
      <p class="contact__role">Consultant</p>
      <ul class="contact__list">
        <li class="contact__item">
          <svg class="contact__icon" viewBox="0 0 16 16" aria-hidden="true"><circle cx="8" cy="8" r="8" fill="#8fa9d6"/><path d="M5 4.5l1.6-.4 1 2-1 .8a5 5 0 0 0 2.5 2.5l.8-1 2 1-.4 1.6c-3.6.2-6.7-2.9-6.5-6.5z" fill="#232326"/></svg>
          555 018 2240
        </li>
        <li class="contact__item">
          <svg class="contact__icon" viewBox="0 0 16 16" aria-hidden="true"><circle cx="8" cy="8" r="8" fill="#8fa9d6"/><rect x="4" y="5.2" width="8" height="5.6" rx=".6" fill="#232326"/><path d="M4.3 5.6L8 8.4l3.7-2.8" stroke="#8fa9d6" stroke-width=".9" fill="none"/></svg>
          info@northridgetc.com
        </li>
        <li class="contact__item">
          <svg class="contact__icon" viewBox="0 0 16 16" aria-hidden="true"><circle cx="8" cy="8" r="8" fill="#8fa9d6"/><g stroke="#232326" stroke-width="1" fill="none"><circle cx="8" cy="8" r="4.2"/><ellipse cx="8" cy="8" rx="1.8" ry="4.2"/><path d="M3.8 8h8.4"/></g></svg>
          www.northridgetc.com
        </li>
      </ul>
    </div>

    <div class="products">
      <div class="product product--scope"><span class="product__mark"></span><div><p class="product__name">Scope</p><p class="product__tag">Device management</p></div></div>
      <div class="product product--beacon"><span class="product__mark"></span><div><p class="product__name">Beacon</p><p class="product__tag">Plunger arrival sensor</p></div></div>
      <div class="product product--tether"><span class="product__mark"></span><div><p class="product__name">Tether</p><p class="product__tag">Device connection</p></div></div>
      <div class="product product--drover"><span class="product__mark"></span><div><p class="product__name">Drover</p><p class="product__tag">Plunger lift controller</p></div></div>
      <div class="product product--strider"><span class="product__mark"></span><div><p class="product__name">Strider</p><p class="product__tag">Plunger velocity sensor</p></div></div>
    </div>
  </section>

</main>
</body>
</html>
```